Business Card Design Project

We need a double-sided business card design for our e-commerce company. Be as creative as you can.

Reason: Change of logo

Target Market(s)

Business owners

Industry/Entity Type

E-Commerce

Requirements
Must have
• Name (editable)
Mobile number -editable
www.trizvo.com - MUST STAND OUT ALONE
Office address:
27 Pellow Road
#09-04 Corbell Tower
Singapore 058214

```html
<!DOCTYPE html>
<html lang="en">
<head>
<meta charset="UTF-8">
<title>Trizvo Business Card</title>
<link href="https://fonts.googleapis.com/css2?family=Montserrat:wght@500;600;700&display=swap" rel="stylesheet">
<style>
  :root {
    --page-bg: #bfe6dc;
    --back-green: #10261a;
    --band-teal: #1d2e35;
    --body-grey: #4b494b;
    --brand-orange: #f07b1f;
    --rule-orange: #c9731e;
    --text-light: #f2f2f2;
  }
  * { margin: 0; padding: 0; box-sizing: border-box; }
  html, body {
    width: 1200px;
    height: 784px;
    overflow: hidden;
    background: var(--page-bg);
    font-family: "Montserrat", sans-serif;
  }
  .sheet {
    position: relative;
    width: 1200px;
    height: 784px;
    display: flex;
    align-items: center;
    justify-content: center;
    gap: 40px;
  }
  .card {
    position: relative;
    width: 540px;
    height: 310px;
    border-radius: 26px;
    overflow: hidden;
    box-shadow: 0 6px 18px rgba(0, 0, 0, 0.18);
  }

  /* Front side */
  .card--front { background: var(--body-grey); }
  .front__band {
    position: absolute;
    top: 0; left: 0; right: 0;
    height: 118px;
    background: var(--band-teal);
  }
  .front__brand {
    position: absolute;
    right: 48px;
    top: 30px;
    font-size: 46px;
    font-weight: 700;
    color: var(--brand-orange);
    letter-spacing: 0.5px;
  }
  .front__details {
    position: absolute;
    left: 48px;
    top: 150px;
    color: var(--text-light);
  }
  .front__name {
    font-size: 17px;
    font-weight: 600;
    margin-bottom: 22px;
  }
  .contact-row {
    display: flex;
    align-items: center;
    gap: 16px;
    font-size: 13px;
    font-weight: 500;
    margin-bottom: 18px;
    white-space: nowrap;
  }
  .contact-row svg { flex: none; }

  /* Back side */
  .card--back { background: var(--back-green); }
  .back__url {
    position: absolute;
    left: 60px;
    top: 120px;
    color: var(--brand-orange);
    font-weight: 700;
    display: flex;
    align-items: baseline;
  }
  .back__url-small { font-size: 16px; }
  .back__url-main { font-size: 50px; letter-spacing: 0.5px; }
  .back__rule {
    position: absolute;
    left: 60px;
    right: 60px;
    top: 190px;
    height: 1px;
    background: var(--rule-orange);
  }
</style>
</head>
<body>
  <main class="sheet">
    <section class="card card--front" aria-label="Business card front">
      <div class="front__band"></div>
      <div class="front__brand">Trizvo</div>
      <div class="front__details">
        <p class="front__name">your name</p>
        <div class="contact-row">
          <svg width="14" height="20" viewBox="0 0 14 20" aria-hidden="true">
            <rect x="1" y="1" width="12" height="18" rx="2" fill="none" stroke="#f2f2f2" stroke-width="1.6"/>
            <line x1="5" y1="15.5" x2="9" y2="15.5" stroke="#f2f2f2" stroke-width="1.4"/>
          </svg>
          <span>xxx xxx xxxxx</span>
        </div>
        <div class="contact-row">
          <svg width="16" height="12" viewBox="0 0 16 12" aria-hidden="true">
            <rect x="0" y="0" width="16" height="12" fill="#f2f2f2"/>
            <polyline points="0,0 8,7 16,0" fill="none" stroke="#4b494b" stroke-width="1.3"/>
          </svg>
          <span>27 Pellow Road,#09-04 Corbell Tower,Singapore 058214</span>
        </div>
      </div>
    </section>

    <section class="card card--back" aria-label="Business card back">
      <div class="back__url">
        <span class="back__url-small">www.</span>
        <span class="back__url-main">trizvo</span>
        <span class="back__url-small">.com</span>
      </div>
      <div class="back__rule"></div>
    </section>
  </main>
</body>
</html>
```